Corvint Property Management Vendor Recruiting Email

We need a digital flyer to email and post on Social media to attract new vendors to our website to apply to complete maintenance work on our clients homes. I have one flyer we had produced recently that we are un-happy with. It is attached.

The example given is what we do not want!! We do not want any of the pictures used from the existing one

Target Market(s)

Construction companies and handyman

Industry/Entity Type

Residential maintenance and repairs

Requirements
Must have
• Join our team as the header not become a vendor

```html
<!DOCTYPE html>
<html lang="en">
<head>
<meta charset="utf-8">
<title>Corvint Property Management – Join Our Team</title>
<link href="https://fonts.googleapis.com/css2?family=Montserrat:wght@400;500;700;800&display=swap" rel="stylesheet">
<style>
  :root {
    --stage: #b3b3b3;
    --ink: #2b2d35;
    --white: #ffffff;
    --purple: #5e3d9c;
    --blue: #2fa8e0;
    --mid-blue: #4f7fc4;
    --text-dark: #2b2d35;
  }
  * { margin: 0; padding: 0; box-sizing: border-box; }
  html, body { width: 1200px; height: 1200px; overflow: hidden; }
  body {
    background: var(--stage);
    font-family: "Montserrat", sans-serif;
    position: relative;
  }
  .flyer {
    position: absolute;
    left: 200px; top: 81px;
    width: 800px; height: 1037px;
    background: var(--white);
    overflow: hidden;
  }
  .flyer-shapes { position: absolute; inset: 0; }
  .brand {
    position: absolute; left: 28px; top: 92px;
    display: flex; align-items: center; gap: 12px;
    color: var(--white); font-weight: 700; font-size: 20px;
    letter-spacing: 0.06em; line-height: 1.2; text-transform: uppercase;
  }
  .brand-square { width: 30px; height: 30px; background: var(--blue); flex: none; }
  .headline { position: absolute; left: 27px; color: var(--white); font-weight: 800; line-height: 1; white-space: nowrap; }
  .headline-top { top: 225px; font-size: 60px; letter-spacing: -0.01em; }
  .headline-main { top: 290px; font-size: 74px; letter-spacing: -0.01em; text-shadow: 2px 2px 0 var(--purple); }
  .benefits { position: absolute; left: 26px; top: 449px; width: 340px; list-style: none; color: var(--white); }
  .benefits li { position: relative; padding-left: 21px; font-size: 19px; line-height: 23.6px; margin-bottom: 16px; white-space: nowrap; }
  .benefits svg { position: absolute; left: 0; top: 5px; }
  .requirements { position: absolute; right: 28px; top: 690px; text-align: right; }
  .req-title { font-weight: 800; font-size: 29px; line-height: 35px; color: var(--text-dark); }
  .req-title .accent {
    background: linear-gradient(90deg, var(--blue), var(--purple));
    -webkit-background-clip: text; background-clip: text; color: transparent;
  }
  .req-list { list-style: none; margin-top: 7px; }
  .req-list li { font-size: 19px; line-height: 27.5px; color: var(--text-dark); padding-right: 24px; position: relative; }
  .req-list svg { position: absolute; right: 0; top: 7px; }
  .phone {
    position: absolute; left: 26px; top: 985px;
    display: flex; align-items: center; gap: 16px;
    color: var(--white); font-weight: 800; font-size: 36px; letter-spacing: -0.01em; line-height: 1;
  }
  .website {
    position: absolute; left: 386px; top: 995px; width: 390px; text-align: center;
    color: var(--white); font-weight: 700; font-size: 17px; letter-spacing: 0.01em; line-height: 1;
  }
</style>
</head>
<body>
  <main class="flyer">
    <svg class="flyer-shapes" width="800" height="1037" viewBox="0 0 800 1037">
      <defs>
        <linearGradient id="band-gradient" x1="0" y1="0" x2="1" y2="0">
          <stop offset="0" stop-color="#5e3d9c"/>
          <stop offset="0.55" stop-color="#4f7fc4"/>
          <stop offset="1" stop-color="#2fa8e0"/>
        </linearGradient>
        <linearGradient id="footer-gradient" x1="0" y1="0" x2="1" y2="0">
          <stop offset="0" stop-color="#2fa8e0"/>
          <stop offset="0.6" stop-color="#4f7fc4"/>
          <stop offset="1" stop-color="#5e3d9c"/>
        </linearGradient>
        <linearGradient id="worker-photo" x1="0" y1="0" x2="1" y2="1">
          <stop offset="0" stop-color="#6f9fd0"/>
          <stop offset="0.5" stop-color="#3f75b8"/>
          <stop offset="1" stop-color="#24508f"/>
        </linearGradient>
        <linearGradient id="scaffold-photo" x1="0" y1="0" x2="1" y2="0">
          <stop offset="0" stop-color="#4a6fb0"/>
          <stop offset="0.45" stop-color="#93a8c4"/>
          <stop offset="1" stop-color="#ffffff" stop-opacity="0"/>
        </linearGradient>
      </defs>

      <rect class="top-panel" x="0" y="0" width="800" height="640" fill="#2b2d35"/>

      <path role="img" aria-label="Photo of a contractor in a blue hard hat adjusting safety goggles" d="M365 484 L390 300 L470 200 L560 130 L600 29 L760 29 L800 190 L800 486 Z" fill="url(#worker-photo)"/>

      <polygon points="0,740 800,641 800,1037 0,1037" fill="#ffffff"/>

      <polygon role="img" aria-label="Photo of a worker in a harness on construction scaffolding" points="0,740 420,688 420,949 0,949" fill="url(#scaffold-photo)"/>

      <polygon points="0,383 800,479 800,486 0,391" fill="#ffffff"/>
      <polygon points="0,391 800,486 800,633 0,732" fill="url(#band-gradient)"/>
      <polygon points="0,732 800,633 800,641 0,740" fill="#2b2d35"/>

      <polygon points="522,322 665,405 665,570 522,653 378,570 378,405" fill="#ffffff"/>
      <polygon role="img" aria-label="Photo of an unfinished room with doors and paint cans" points="522,337 651,413 651,562 522,638 392,562 392,413" fill="#b9b8b2"/>

      <polygon points="0,949 326,949 366,1037 0,1037" fill="#2b2d35"/>
      <polygon points="336,971 800,971 800,1037 366,1037" fill="#ffffff"/>
      <polygon points="346,971 800,971 800,1037 376,1037" fill="url(#footer-gradient)"/>
    </svg>

    <div class="brand">
      <span class="brand-square"></span>
      <span>Corvint Property<br>Management</span>
    </div>

    <h1 class="headline headline-top">JOIN OUR</h1>
    <p class="headline headline-main">TEAM</p>

    <ul class="benefits">
      <li><svg width="13" height="13" viewBox="0 0 13 13"><path d="M2 7 L5 10 L11 2" fill="none" stroke="#fff" stroke-width="2"/></svg>95% approval rating on all<br>submitted estimates.<br>Guaranteed work volume.</li>
      <li><svg width="13" height="13" viewBox="0 0 13 13"><path d="M2 7 L5 10 L11 2" fill="none" stroke="#fff" stroke-width="2"/></svg>Material purchasing program<br>to help vendors with low<br>capital or no or bad credit.</li>
      <li><svg width="13" height="13" viewBox="0 0 13 13"><path d="M2 7 L5 10 L11 2" fill="none" stroke="#fff" stroke-width="2"/></svg>Weekly secure direct deposit<br>with net30 payment terms,</li>
    </ul>

    <section class="requirements">
      <h2 class="req-title">REQUIREMENTS TO<br><span class="accent">JOIN OUR TEAM</span></h2>
      <ul class="req-list">
        <li>Auto insurance<svg width="13" height="13" viewBox="0 0 13 13"><path d="M2 7 L5 10 L11 2" fill="none" stroke="#4f7fc4" stroke-width="2"/></svg></li>
        <li>Certificate of general liability insurance<svg width="13" height="13" viewBox="0 0 13 13"><path d="M2 7 L5 10 L11 2" fill="none" stroke="#4f7fc4" stroke-width="2"/></svg></li>
        <li>Workman's compensation or state issued<br>exemption letter<svg width="13" height="13" viewBox="0 0 13 13"><path d="M2 7 L5 10 L11 2" fill="none" stroke="#4f7fc4" stroke-width="2"/></svg></li>
        <li>Drive license or state issued IDcard<svg width="13" height="13" viewBox="0 0 13 13"><path d="M2 7 L5 10 L11 2" fill="none" stroke="#4f7fc4" stroke-width="2"/></svg></li>
        <li>Coverage area<svg width="13" height="13" viewBox="0 0 13 13"><path d="M2 7 L5 10 L11 2" fill="none" stroke="#4f7fc4" stroke-width="2"/></svg></li>
        <li>Any specialty licenses<svg width="13" height="13" viewBox="0 0 13 13"><path d="M2 7 L5 10 L11 2" fill="none" stroke="#4f7fc4" stroke-width="2"/></svg></li>
      </ul>
    </section>

    <div class="phone">
      <svg width="28" height="28" viewBox="0 0 24 24"><path d="M6.6 10.8c1.4 2.8 3.8 5.1 6.6 6.6l2.2-2.2c.3-.3.7-.4 1-.2 1.1.4 2.3.6 3.6.6.6 0 1 .4 1 1V20c0 .6-.4 1-1 1C10.6 21 3 13.4 3 4c0-.6.4-1 1-1h3.5c.6 0 1 .4 1 1 0 1.3.2 2.5.6 3.6.1.3 0 .7-.2 1L6.6 10.8z" fill="#4f7fc4"/></svg>
      <span>555-014-2290</span>
    </div>
    <p class="website">WWW.CORVINTPROPERTY.COM</p>
  </main>
</body>
</html>
```